Web Design Project

Revamp current website adding newly designed logo and creating layout that is good on desktops, tablets, and cell phones.

Current website can be viewed at www.venkirainteriors.com

Will you see the website is small but graphics heavy in the gallery. The gallery needs to be setup so that it is easy to maintain the links and update the photos.

Needs to have high visual impact.

I need a new logo and website layout designed for my partner's business. This is a birthday present. His business is interior painting, wallpapering and design. He also has access to a wide variety of products including carpet, fabrics, furniture, wallpaper, tile, countertops, etc. I have attached some screen shots of his website for reference. He is a one man shop and has a stellar reputation with his customers. He is on-time, very tidy, excellent with animals, and always finishes on time and on budget. There are no restrictions on colors or fonts. The logo needs to work well with the website, business cards and printed materials. The website needs to flow content for device size so it looks just as good on a cell phone or tablet as it does on a desktop computer. Whatever the heck that's called! Thanks. I am looking forward to seeing everyone's ideas.

Target Market(s)

Consumers looking for interior design, painting, and wallpapering as well as interior products such as flooring, window treatments, reupholstering, counter tops, etc.

Industry/Entity Type

Cell Phone

Requirements
Must have
• Clean, sharp, visual impact (at least on the home page)
Should not have
• Clutter.

```html
<!DOCTYPE html>
<html lang="en">
<head>
<meta charset="utf-8">
<title>Venkira Interior Designs</title>
<link href="https://fonts.googleapis.com/css2?family=Roboto:wght@300;400;500&family=Roboto+Condensed:wght@300;400&family=Great+Vibes&display=swap" rel="stylesheet">
<style>
:root{
  --brand:#c4005a;
  --plum:#5a0f2e;
  --ink:#3a3a3a;
  --body:#8a8a8a;
  --rule:#c9c3c3;
  --panel:#f6f2f1;
  --carpet:#cc0a62;
  --fabric:#7db86c;
  --furniture:#f9a843;
  --wallpaper:#4cb4c4;
  --white:#ffffff;
}
*{box-sizing:border-box;margin:0;padding:0}
html,body{width:756px;height:1200px;overflow:hidden;background:var(--white)}
body{position:relative;font-family:'Roboto',sans-serif;color:var(--ink)}
.abs{position:absolute}

.brand{left:48px;top:40px;display:flex;align-items:center;gap:8px}
.brand-dot{width:14px;height:14px;border-radius:50%;background:var(--brand)}
.brand-name{font-family:'Roboto',sans-serif;font-weight:400;font-size:18px;color:var(--brand)}

.phone{right:52px;top:14px;font-size:11.5px;color:var(--brand);display:flex;align-items:center;gap:4px;letter-spacing:.3px}
.nav{right:52px;top:57px;display:flex;gap:20px;font-family:'Roboto Condensed',sans-serif;font-size:10px;color:var(--ink)}
.nav a{color:inherit;text-decoration:none;position:relative}
.nav .current{color:var(--brand)}
.nav .current::after{content:"";position:absolute;left:0;right:0;top:14px;height:2px;background:var(--brand)}

.hero{left:48px;top:100px;width:658px;height:352px;
  background:radial-gradient(ellipse at 50% 30%,#efe3c4 0%,#c9ae7c 45%,#8a6a42 80%,#5e4327 100%)}
.hero-line{left:0;right:0;top:112px;text-align:center;font-family:'Great Vibes',cursive;font-size:58px;line-height:70px;color:var(--white);text-shadow:0 2px 4px rgba(0,0,0,.45)}
.hero-more{left:302px;top:236px;width:46px;height:24px;background:var(--white);color:var(--plum);font-size:9.5px;display:flex;align-items:center;justify-content:center;transform:skewX(-8deg)}

.tile{top:454px;height:53px;width:133px;color:var(--white);font-family:'Roboto Condensed',sans-serif;font-size:17px;display:flex;align-items:flex-end;justify-content:center;padding-bottom:7px;border-top:2px solid rgba(255,255,255,.7)}
.tile svg{position:absolute;left:44px;top:-22px}
.carpet{left:105px;background:var(--carpet)}
.fabric{left:243px;background:var(--fabric)}
.furniture{left:381px;background:var(--furniture)}
.wallpaper{left:518px;background:var(--wallpaper)}

.h2{font-family:'Roboto Condensed',sans-serif;font-weight:400;font-size:17px;color:var(--plum);letter-spacing:.2px}
.h2 em{font-style:normal;color:var(--brand)}
.rule{height:2px;border-top:1px solid var(--rule);border-bottom:1px solid var(--rule)}

.welcome{left:0;width:756px;top:530px;text-align:center}
.welcome-rule{left:313px;top:556px;width:130px}
.intro{left:108px;width:540px;top:574px;text-align:center;font-weight:300;font-size:9.4px;line-height:12px;color:var(--body)}
.intro p{margin-bottom:7.5px}

.panel{left:48px;top:710px;width:658px;height:246px;background:var(--panel)}
.services-h{left:105px;top:728px}
.services-rule{left:105px;top:754px;width:76px}
.gallery-h{left:378px;top:728px}
.gallery-rule{left:378px;top:754px;width:112px}
.svc{left:106px;width:256px;display:flex;gap:7px;font-weight:300;font-size:8.2px;line-height:10.5px;color:#6e6e6e}
.svc svg{flex:none}
.grid{left:378px;top:775px;width:272px;height:141px;display:grid;grid-template-columns:repeat(3,1fr);grid-template-rows:repeat(2,1fr);gap:1px;background:var(--white)}
.grid div:nth-child(1){background:linear-gradient(135deg,#c21f2a,#e9d7d2)}
.grid div:nth-child(2){background:linear-gradient(135deg,#9a9a9a,#4e4e4e)}
.grid div:nth-child(3){background:linear-gradient(135deg,#555,#c9c9c9)}
.grid div:nth-child(4){background:linear-gradient(135deg,#aaa,#6a6a6a)}
.grid div:nth-child(5){background:linear-gradient(135deg,#3c3c3c,#8c8c8c)}
.grid div:nth-child(6){background:linear-gradient(135deg,#2a2a2a,#d9d9d9)}

.news-h{left:106px;top:982px}
.news-rule{left:106px;top:1008px;width:74px}
.video-h{left:441px;top:982px}
.video-rule{left:441px;top:1008px;width:96px}
.news{top:1038px;height:56px}
.news .date{position:absolute;left:0;top:0;width:18px;height:18px;background:var(--plum);color:var(--white);font-size:5.5px;line-height:6.5px;padding:2px 0 0 3px;font-weight:500}
.news .meta{position:absolute;left:4px;top:24px}
.news .photo{position:absolute;left:18px;top:0;right:0;bottom:0}
.news .cap{position:absolute;left:18px;top:60px;font-size:6px;font-weight:500;color:var(--plum);white-space:nowrap}
.video{top:1025px;width:102px;height:75px;display:flex;align-items:center;justify-content:center}

.footer-line{left:48px;top:1142px;width:658px;height:1px;background:#e2dede}
.copy{left:106px;top:1160px;font-size:6.5px;color:#a5a5a5}
.copy span{color:var(--brand)}
.social{left:495px;top:1153px;display:flex;gap:6.5px}
.social i{width:21px;height:21px;border-radius:50%;border:1px solid #c8c8c8;display:block}
.social i.on{border-color:#3b5998}
.bottom-line{left:48px;top:1186px;width:658px;height:2px;background:#e4e0e0}
</style>
</head>
<body>

<header>
  <div class="abs brand"><span class="brand-dot"></span><span class="brand-name">Venkira Interior Designs</span></div>
  <div class="abs phone">
    <svg width="10" height="10" viewBox="0 0 24 24"><path fill="#5a0f2e" d="M6.6 10.8a15 15 0 0 0 6.6 6.6l2.2-2.2c.3-.3.7-.4 1-.2 1.1.4 2.300.6 3.6.6.6 0 1 .4 1 1V20c0 .6-.4 1-1 1A17 17 0 0 1 3 4c0-.6.4-1 1-1h3.5c.6 0 1 .4 1 1 0 1.3.2 2.5.6 3.6.1.3 0 .7-.2 1z"/></svg>
    555.014.2287
  </div>
  <nav class="abs nav">
    <a class="current">HOME</a><a>ABOUT</a><a>CONTACT</a><a>GALLERY</a><a>PRODUCTS</a><a>SERVICES</a>
  </nav>
</header>

<section class="abs hero" role="img" aria-label="Bright sitting room with two cream sofas, tall windows and a rose rug">
  <div class="abs hero-line">Beautiful Happens.</div>
  <div class="abs hero-more">MORE</div>
</section>

<div class="abs tile carpet">
  <svg width="44" height="44" viewBox="0 0 44 44"><polygon points="22,2 40,12 40,32 22,42 4,32 4,12" fill="var(--carpet)" stroke="#fff" stroke-width="2"/><circle cx="22" cy="22" r="7" fill="none" stroke="#fff" stroke-width="2.5"/></svg>
  CARPET
</div>
<div class="abs tile fabric">
  <svg width="44" height="44" viewBox="0 0 44 44"><polygon points="22,2 40,12 40,32 22,42 4,32 4,12" fill="var(--fabric)" stroke="#fff" stroke-width="2"/><rect x="13" y="17" width="18" height="10" rx="3" fill="#fff"/></svg>
  FABRIC
</div>
<div class="abs tile furniture">
  <svg width="44" height="44" viewBox="0 0 44 44"><polygon points="22,2 40,12 40,32 22,42 4,32 4,12" fill="var(--furniture)" stroke="#fff" stroke-width="2"/><path d="M12 26v-6h20v6M14 20v-3h16v3M12 26h20" fill="none" stroke="#fff" stroke-width="2"/></svg>
  FURNITURE
</div>
<div class="abs tile wallpaper">
  <svg width="44" height="44" viewBox="0 0 44 44"><polygon points="22,2 40,12 40,32 22,42 4,32 4,12" fill="var(--wallpaper)" stroke="#fff" stroke-width="2"/><rect x="13" y="16" width="18" height="13" fill="none" stroke="#fff" stroke-width="2"/></svg>
  WALLPAPER
</div>

<h1 class="abs h2 welcome">WELCOME TO <em>VENKIRA INTERIOR DESIGNS</em></h1>
<div class="abs rule welcome-rule"></div>
<div class="abs intro">
  <p>With the various materials, colors, and finishes available the choices today can be daunting. By listening to you, I am able to pick just the right color, the right fabric, or the right furniture for your projects.</p>
  <p>Whether you are starting with a small project or a large project, I am ready to bring your ideas to life. It doesn't take a big budget to achieve dramatic effects. A wonderful new look is within anyone's reach.</p>
  <p>My guidance with the selection of colors, fabrics, paint, wallpaper, and furniture, as well as the placement of items in a room, will help you achieve the results you desire – a beautiful home that is a joy to walk into and to show off!</p>
  <p>Your home is a reflection of your personality. Let it tell people how wonderful you are.</p>
</div>

<section class="abs panel"></section>
<h2 class="abs h2 services-h">OUR <em>SERVICES</em></h2>
<div class="abs rule services-rule"></div>
<h2 class="abs h2 gallery-h">OUR <em>PHOTO GALLERY</em></h2>
<div class="abs rule gallery-rule"></div>

<div class="abs svc" style="top:773px"><svg width="14" height="20" viewBox="0 0 14 20"><path d="M3 18L7 2h6L9 18z" fill="var(--brand)"/></svg><span>I can you choose the correct color necessary to give you that finished look for your home. These colors can complement your existing or new furniture.</span></div>
<div class="abs svc" style="top:815px"><svg width="14" height="20" viewBox="0 0 14 20"><path d="M3 18L7 2h6L9 18z" fill="var(--brand)"/></svg><span>I will perform any interior painting and wallpapering myself to ensure the perfect finish.</span></div>
<div class="abs svc" style="top:846px"><svg width="14" height="20" viewBox="0 0 14 20"><path d="M3 18L7 2h6L9 18z" fill="var(--brand)"/></svg><span>I can provide guidance with the style selection of furniture periods, such as Modern, Contemporary, Provincial, Traditional, Mission and others.</span></div>
<div class="abs svc" style="top:888px"><svg width="14" height="20" viewBox="0 0 14 20"><path d="M3 18L7 2h6L9 18z" fill="var(--brand)"/></svg><span>I can provide in-home consultation and offer guidance concerning space planning, furniture arrangement and solutions for your everyday concerns</span></div>
<svg class="abs" style="left:127px;top:930px" width="16" height="8" viewBox="0 0 16 8"><path d="M0 4h14M11 1l3 3-3 3" fill="none" stroke="#777" stroke-width="1"/></svg>

<div class="abs grid" role="img" aria-label="Gallery of six finished interior rooms">
  <div></div><div></div><div></div><div></div><div></div><div></div>
</div>
<svg class="abs" style="left:633px;top:936px" width="16" height="8" viewBox="0 0 16 8"><path d="M0 4h14M11 1l3 3-3 3" fill="none" stroke="#777" stroke-width="1"/></svg>

<h2 class="abs h2 news-h">LATEST <em>NEWS</em></h2>
<div class="abs rule news-rule"></div>
<h2 class="abs h2 video-h">RECENT <em>PVIDEOS</em></h2>
<div class="abs rule video-rule"></div>

<article class="abs news" style="left:106px;width:97px">
  <div class="date">06<br>SEP</div>
  <svg class="meta" width="10" height="20" viewBox="0 0 10 20"><rect x="1" y="1" width="8" height="5" fill="none" stroke="#999" stroke-width=".8"/><path d="M5 17l-3-3a1.6 1.6 0 0 1 3-1.5 1.6 1.6 0 0 1 3 1.5z" fill="none" stroke="#999" stroke-width=".8"/></svg>
  <div class="photo" role="img" aria-label="Designer presenting samples at an event" style="background:linear-gradient(135deg,#8a7a64,#d9cdb8)"></div>
  <div class="cap">Lorem ipsum dolor siteetc</div>
</article>
<article class="abs news" style="left:210px;width:89px">
  <div class="date">06<br>SEP</div>
  <svg class="meta" width="10" height="20" viewBox="0 0 10 20"><rect x="1" y="1" width="8" height="5" fill="none" stroke="#999" stroke-width=".8"/><path d="M5 17l-3-3a1.6 1.6 0 0 1 3-1.5 1.6 1.6 0 0 1 3 1.5z" fill="none" stroke="#999" stroke-width=".8"/></svg>
  <div class="photo" role="img" aria-label="Client portrait in warm red tones" style="background:linear-gradient(135deg,#d9452e,#f0b08a)"></div>
  <div class="cap">Lorem ipsum dolor siteetc</div>
</article>
<article class="abs news" style="left:311px;width:98px">
  <div class="date">06<br>SEP</div>
  <svg class="meta" width="10" height="20" viewBox="0 0 10 20"><rect x="1" y="1" width="8" height="5" fill="none" stroke="#999" stroke-width=".8"/><path d="M5 17l-3-3a1.6 1.6 0 0 1 3-1.5 1.6 1.6 0 0 1 3 1.5z" fill="none" stroke="#999" stroke-width=".8"/></svg>
  <div class="photo" role="img" aria-label="Designer reviewing colour swatches at a desk" style="background:linear-gradient(135deg,#e8e4dc,#b9a58c)"></div>
  <div class="cap">Lorem ipsum dolor siteetc</div>
</article>

<div class="abs video" style="left:439px;background:linear-gradient(135deg,#e8e6e2,#9c928a)" role="img" aria-label="Video of a designer sketching a room plan">
  <svg width="36" height="36" viewBox="0 0 36 36"><circle cx="18" cy="18" r="16" fill="none" stroke="#fff" stroke-width="2.5"/><path d="M14 11l11 7-11 7z" fill="#fff"/></svg>
</div>
<div class="abs video" style="left:549px;background:linear-gradient(135deg,#3a2618,#a57a4c)" role="img" aria-label="Video of a consultation in a finished kitchen">
  <svg width="36" height="36" viewBox="0 0 36 36"><circle cx="18" cy="18" r="16" fill="none" stroke="#fff" stroke-width="2.5"/><path d="M14 11l11 7-11 7z" fill="#fff"/></svg>
</div>

<footer>
  <div class="abs footer-line"></div>
  <div class="abs copy">© 2014 <span>Venkira Interior Designs.</span> All Rights Reserved</div>
  <div class="abs social"><i></i><i class="on"></i><i></i><i></i><i></i><i></i></div>
  <div class="abs bottom-line"></div>
</footer>

</body>
</html>
```